Larkmoor Heritage Guild Harvest Lantern Days Event Flyer - Historic Event

I need a flyer about the Larkmoor Heritage Guild's Harvest Lantern Days event October 8th and 9th. The centerpiece of Harvest Lantern Days is Civil War reenactments. I want the flyer to include the schedule of events and be eye catching on area bulletin boards. Our website is www.larkmoorheritageguild.org for more information and pictures. The website for the Tilden Rangers reenactors is http://www.tildenrangers.com/.

Target Market(s)

Our target market is middle ages (35-70) families and couples. Most are history buffs, especially about the Civil War.

Industry/Entity Type

Non-Profit

Font styles to use
Serif
Decorative
Script

Requirements
Must have
• The flyer must include the majority of the schedule attached - especially the battle times, museums, and anything including food.The dance on Saturday night is also important. The bottom of the flyer MUST say "Paid in part by Osgood County Visitor Fund Board"
Nice to have
• Pictures

```html
<!DOCTYPE html>
<html lang="en">
<head>
<meta charset="utf-8">
<title>Larkmoor Heritage Guild – Harvest Lantern Days</title>
<link rel="stylesheet" href="https://fonts.googleapis.com/css2?family=Cinzel:wght@500&family=Sofia&family=Tinos:ital,wght@0,700;1,700&family=Alegreya+SC:wght@700&display=swap">
<style>
  :root {
    --ink: #111;
    --gold-dark: #8a5a1c;
    --gold-mid: #c8974f;
    --gold-light: #e2bf7d;
    --cream: #f7ebc0;
    --cream-light: #fbf3d3;
    --orange: #e8862a;
    --red: #a51d1d;
    --brown-deep: #2a140a;
    --frame: #e9e6de;
  }
  html, body { margin: 0; padding: 0; }
  body {
    width: 900px; height: 1200px; overflow: hidden;
    background: #1e1e1e;
    font-family: "Tinos", "Times New Roman", serif;
    color: var(--ink);
  }
  .flyer { position: relative; width: 900px; height: 1200px; overflow: hidden; }

  .masthead {
    position: absolute; left: 0; top: 0; width: 900px; height: 336px;
    background: radial-gradient(ellipse at 55% 45%, var(--gold-light) 0%, var(--gold-mid) 55%, var(--gold-dark) 100%);
    border-bottom: 5px solid #b07a35;
    box-sizing: border-box;
  }
  .guild-band {
    position: absolute; left: 0; top: 27px; width: 900px; height: 52px;
    background: #050505;
    display: flex; align-items: center; justify-content: center;
    font-family: "Cinzel", serif; font-size: 29px; letter-spacing: 7px;
    color: var(--orange);
  }
  .event-title {
    position: absolute; left: 0; top: 92px; width: 900px; margin: 0;
    font-family: "Sofia", cursive; font-weight: 400; color: var(--ink);
    text-align: center; line-height: 1;
  }
  .event-title .line-one { display: block; font-size: 96px; padding-left: 190px; }
  .event-title .line-two { display: block; font-size: 96px; margin-top: -14px; padding-left: 40px; }

  .schedule-panel {
    position: absolute; left: 0; top: 336px; width: 900px; height: 512px;
    background: linear-gradient(90deg, var(--cream-light) 0%, var(--cream) 60%, #f0d99a 100%);
  }
  .photo {
    position: absolute; box-sizing: border-box;
    border: 5px double var(--frame); border-radius: 22px;
    outline: 2px solid #fff; outline-offset: -2px;
  }
  .photo-river { left: 15px; top: 4px; width: 260px; height: 246px;
    background: linear-gradient(180deg, #d8c6b5 0%, #3d5a2a 40%, #6f6a62 62%, #8a8a84 100%); }
  .photo-dining { left: 15px; top: 259px; width: 260px; height: 248px;
    background: linear-gradient(180deg, #d6c7a8 0%, #7a4d32 50%, #efeae1 75%, #6a3d2a 100%); }

  .schedule { position: absolute; left: 303px; top: 12px; width: 590px; }
  .day-heading {
    margin: 0; font-family: "Alegreya SC", serif; font-size: 25px; color: var(--red);
    line-height: 26px;
  }
  .day-note { margin: 0 0 14px; font-style: italic; font-size: 15.5px; }
  .day-list { margin: 0; padding: 0; list-style: none; font-size: 16.5px; line-height: 21px; }
  .day-list li { display: flex; }
  .day-list .time { width: 100px; flex: none; }
  .day-list .what { border-left: 1.5px solid var(--ink); padding-left: 6px; }
  .day-list .sponsor { display: block; font-size: 12.5px; line-height: 22px; padding-left: 4px; }
  .sunday { margin-top: 8px; }

  .gallery {
    position: absolute; left: 0; top: 848px; width: 900px; height: 301px;
    background: var(--brown-deep);
  }
  .photo-tent { left: 15px; top: 16px; width: 278px; height: 264px;
    background: linear-gradient(180deg, #c89a5a 0%, #e8e3d6 35%, #7a5a38 70%, #3f3a2a 100%); }
  .photo-cabin { left: 311px; top: 16px; width: 278px; height: 264px;
    background: linear-gradient(180deg, #6f9a3c 0%, #a39b8c 35%, #8a6a48 65%, #6e8a44 100%); }
  .photo-band { left: 607px; top: 16px; width: 278px; height: 264px;
    background: linear-gradient(180deg, #4c6a3a 0%, #3a3a36 50%, #6f7a4a 100%); }

  .funding-strip {
    position: absolute; left: 0; top: 1149px; width: 900px; height: 51px;
    background: linear-gradient(90deg, #7a3c16, #a85a24 50%, #7a3c16);
    display: flex; align-items: center; justify-content: center;
    color: #fff; font-size: 24px; font-weight: 700;
  }
</style>
</head>
<body>
<main class="flyer">
  <header class="masthead">
    <div class="guild-band">LARKMOOR HERITAGE GUILD'S</div>
    <h1 class="event-title">
      <span class="line-one">Harvest Lantern</span>
      <span class="line-two">Days event</span>
    </h1>
  </header>

  <section class="schedule-panel">
    <div class="photo photo-river" role="img" aria-label="Photo of a wooded river bank at dusk"></div>
    <div class="photo photo-dining" role="img" aria-label="Photo of a historic house dining room with a violinist and visitors"></div>

    <div class="schedule">
      <h2 class="day-heading">Saturday, October 8th, 2016</h2>
      <p class="day-note">Through the Day – Demonstrations and Speakers in various locations</p>
      <ul class="day-list">
        <li><span class="time">10:00 AM</span><span class="what">Battle by Tilden Rangers<span class="sponsor">Sponsored in part by Hollis Corner Stores</span></span></li>
        <li><span class="time">11:30-1:00</span><span class="what">Chicken Biscuit Bake at Town Hall – Free Will Donation</span></li>
        <li><span class="time">Afternoon</span><span class="what">Trolley and Buggy Rides</span></li>
        <li><span class="time">1:00-4:00</span><span class="what">Museums Opens</span></li>
        <li><span class="time">1:30-2:00</span><span class="what">Birthday Cake on Ellery House Front Porch<span class="sponsor">Cake donated by Marlow Grocers- Pike City</span></span></li>
        <li><span class="time">2:00 PM</span><span class="what">Battle by Tilden Rangers</span></li>
        <li><span class="time">3:00 PM</span><span class="what">Sightseeing Cruise on the Spirit of Larkmoor</span></li>
        <li><span class="time">6:00 PM</span><span class="what">? Dance at Town Hall with Ridgeline Band<span class="sponsor">Sponsored by Dr. Whitcombe</span></span></li>
      </ul>

      <h2 class="day-heading sunday">Sunday, October 9th, 2016</h2>
      <ul class="day-list">
        <li><span class="time">12:30 PM</span><span class="what">Parade on Main Street</span></li>
        <li><span class="time">Afternoon</span><span class="what">Buggy &amp; Trolley Rides</span></li>
        <li><span class="time">1:00-4:00</span><span class="what">Museums Open</span></li>
        <li><span class="time">1:30 PM</span><span class="what">Battle by Tilden Rangers</span></li>
        <li><span class="time">2:00 PM</span><span class="what">Pie Reception at Larkmoor Depot and<br>Railroad History Museum</span></li>
        <li><span class="time">3:00 PM</span><span class="what">Sightseeing Cruise</span></li>
      </ul>
    </div>
  </section>

  <section class="gallery">
    <div class="photo photo-tent" role="img" aria-label="Photo of a canvas-roofed wagon shelter with reenactors"></div>
    <div class="photo photo-cabin" role="img" aria-label="Photo of a small log cabin among trees"></div>
    <div class="photo photo-band" role="img" aria-label="Photo of period-dressed musicians playing fiddles and bass outdoors"></div>
  </section>

  <footer class="funding-strip">Paid in part by Osgood County Visitor Fund Board</footer>
</main>
</body>
</html>
```